A4 Flyer

Bright Path Learning is starting a course in regional Victoria. We are currently advertising (See attached file A34984) in local papers but need to create a one page flyer to distribute to Aged Care facilities in the area. The A4 flyer will be inserted into a folder pack with more detailed information on Bright Path Learning. Important to use images and logoes attached

Target Market(s)

Flyer to be distributed to Aged Care facility staff and owners

Industry/Entity Type

Advertising

Font styles to use
Sans Serif

Colors
f37123
ec1f27

Requirements
Must have
• BPL Logo
Some image

```html
<!DOCTYPE html>
<html lang="en">
<head>
<meta charset="utf-8">
<title>Bright Path Learning – Fast Track Course Flyer</title>
<link rel="stylesheet" href="https://fonts.googleapis.com/css2?family=Questrial&family=Oswald:wght@400;500;600&display=swap">
<style>
  :root {
    --orange: #f37123;
    --red: #ec1f27;
    --blue: #1a6db5;
    --blue-dark: #0f5ea8;
    --yellow: #fdc82f;
    --cream: #fde9b8;
    --peach: #fbb563;
    --text-dark: #4a4a4a;
    --white: #ffffff;
  }
  * { margin: 0; padding: 0; box-sizing: border-box; }
  html, body { width: 849px; height: 1200px; overflow: hidden; background: var(--white); }
  .flyer {
    position: relative; width: 849px; height: 1200px; overflow: hidden;
    background: linear-gradient(160deg, #fff6dc 0%, var(--cream) 25%, var(--peach) 70%, #f8a24a 100%);
    font-family: "Questrial", sans-serif;
  }
  .headline-band {
    position: absolute; top: 0; left: 0; width: 100%; height: 121px;
    background: var(--orange); color: var(--white);
    font-size: 78px; line-height: 121px; text-align: center; letter-spacing: 1px;
  }
  .course-band {
    position: absolute; top: 121px; left: 0; width: 100%; height: 72px;
    background: var(--blue); color: var(--white);
    font-size: 40px; line-height: 72px; text-align: center;
  }
  .course-band em { font-style: italic; }
  .course-band strong { font-family: "Oswald", sans-serif; font-weight: 500; letter-spacing: .5px; }
  .qualification-callout { position: absolute; left: 134px; top: 176px; width: 576px; height: 112px; }
  .qualification-text {
    position: absolute; left: 137px; top: 210px; width: 570px; text-align: center;
    font-family: "Oswald", sans-serif; color: var(--text-dark);
  }
  .qualification-text .title { font-size: 25px; font-weight: 600; line-height: 30px; }
  .qualification-text .subtitle { font-size: 24px; font-style: italic; line-height: 32px; transform: skewX(-8deg); }
  .venue {
    position: absolute; top: 302px; left: 0; width: 100%; text-align: center;
    font-family: "Oswald", sans-serif; font-weight: 600; font-size: 29px; color: var(--blue-dark);
    letter-spacing: .3px;
  }
  .unit-list { position: absolute; left: 30px; top: 368px; list-style: none; }
  .unit-list li {
    position: relative; padding-left: 33px; font-size: 29px; line-height: 40px; color: var(--text-dark);
  }
  .unit-list li::before {
    content: ""; position: absolute; left: 2px; top: 14px; width: 13px; height: 13px;
    border-radius: 50%; background: var(--orange);
  }
  .funding-note {
    position: absolute; left: 46px; font-family: "Oswald", sans-serif; font-size: 20px;
    line-height: 25px; color: var(--orange); padding-left: 18px; text-indent: -18px;
  }
  .funding-note.fees { top: 718px; width: 200px; }
  .funding-note.delivery { top: 830px; width: 190px; }
  .photo {
    position: absolute; border-radius: 50%; border: 10px solid var(--white);
    box-shadow: 0 4px 14px rgba(0,0,0,.18);
  }
  .photo.trainer { left: 440px; top: 365px; width: 330px; height: 330px;
    background: radial-gradient(circle at 60% 45%, #d9463a 0%, #e9c9a8 35%, #f1ece6 70%); }
  .photo.student-man { left: 248px; top: 660px; width: 262px; height: 262px;
    background: radial-gradient(circle at 50% 45%, #7a5236 0%, #b6a89a 45%, #eceae7 75%); }
  .photo.student-woman { left: 528px; top: 725px; width: 268px; height: 268px;
    background: radial-gradient(circle at 50% 40%, #8c5a3c 0%, #3a2a26 45%, #e6e2de 80%); }
  .flow-arrows { position: absolute; left: 0; top: 0; width: 849px; height: 1200px; pointer-events: none; }
  .footer-waves { position: absolute; left: 0; top: 1000px; width: 849px; height: 80px; }
  .footer {
    position: absolute; left: 0; top: 1060px; width: 100%; height: 140px; background: var(--blue);
  }
  .brand { position: absolute; left: 62px; top: 40px; display: flex; align-items: center; gap: 16px; }
  .brand-dot { width: 58px; height: 58px; border-radius: 50%; background: var(--orange); }
  .brand-name { font-size: 36px; line-height: 38px; color: var(--orange); width: 220px; }
  .enrol { position: absolute; right: 48px; top: 20px; text-align: center; width: 390px; }
  .enrol .label { font-family: "Oswald", sans-serif; font-weight: 600; font-size: 22px; color: var(--orange); }
  .enrol .url { font-size: 29px; color: var(--white); line-height: 40px; }
  .enrol .call { font-family: "Oswald", sans-serif; font-size: 25px; color: var(--yellow); font-style: italic; }
  .enrol .call strong { font-style: normal; font-weight: 600; }
</style>
</head>
<body>
<main class="flyer">
  <header class="headline-band">Unique Opportunity!</header>
  <div class="course-band"><em>Fast Track Course</em> – <strong>Starts July 2014</strong></div>

  <svg class="qualification-callout" viewBox="0 0 576 112" aria-hidden="true">
    <path d="M14 30 H455 L475 12 L495 30 H562 Q572 30 572 40 V98 Q572 108 562 108 H14 Q4 108 4 98 V40 Q4 30 14 30 Z"
          fill="#fdc82f" stroke="#f37123" stroke-width="4"/>
  </svg>
  <div class="qualification-text">
    <div class="title">~ DOUBLE QUALIFICATION ~</div>
    <div class="subtitle">CERT III IN AGED CARE WITH HOME &amp; COMMUNITY CARE</div>
  </div>

  <div class="venue">RIVERSIDE NURSING HOME – WESTBROOK, 9.00AM - 3.00PM</div>

  <ul class="unit-list">
    <li>Pathology</li>
    <li>Aged Care</li>
    <li>First Aid</li>
    <li>CPR</li>
    <li>Anaphylaxis</li>
    <li>Home &amp; Community Care</li>
    <li>Medications for PCA’s</li>
    <li>Health Services</li>
  </ul>

  <p class="funding-note fees">~ Government Funding for eligible students! Fees from $117</p>
  <p class="funding-note delivery">~ This training is delivered with VIC and Comm. Govt. Funding to eligible students.</p>

  <div class="photo trainer" role="img" aria-label="Trainer pointing to an anatomical torso model"></div>
  <div class="photo student-man" role="img" aria-label="Smiling male student portrait"></div>
  <div class="photo student-woman" role="img" aria-label="Smiling female student portrait"></div>

  <svg class="flow-arrows" viewBox="0 0 849 1200" aria-hidden="true">
    <path d="M442 372 Q372 400 366 505" fill="none" stroke="#f37123" stroke-width="4"/>
    <path d="M353 498 L366 520 L380 498 Z" fill="#f37123"/>
    <path d="M388 962 Q280 965 248 895" fill="none" stroke="#f37123" stroke-width="4"/>
    <path d="M238 906 L244 882 L262 898 Z" fill="#f37123"/>
    <path d="M756 1020 Q815 985 828 922" fill="none" stroke="#ffffff" stroke-width="4"/>
    <path d="M816 928 L832 905 L842 932 Z" fill="#ffffff"/>
  </svg>

  <svg class="footer-waves" viewBox="0 0 849 80" preserveAspectRatio="none" aria-hidden="true">
    <path d="M0 30 Q420 10 849 32 V80 H0 Z" fill="#f37123"/>
    <path d="M0 40 Q420 20 849 44 V80 H0 Z" fill="#fdc82f"/>
    <path d="M0 50 Q420 32 849 54 V80 H0 Z" fill="#ffffff"/>
    <path d="M0 58 Q420 42 849 62 V80 H0 Z" fill="#1a6db5"/>
  </svg>

  <footer class="footer">
    <div class="brand">
      <span class="brand-dot" aria-hidden="true"></span>
      <span class="brand-name">Bright Path Learning</span>
    </div>
    <div class="enrol">
      <div class="label">TO ENROL VISIT</div>
      <div class="url">www.brightpathlearning.com.au</div>
      <div class="call">OR CALL: <strong>9555 0142</strong></div>
    </div>
  </footer>
</main>
</body>
</html>
```